Premium Personal Brand — Facebook Banner (Used Across All Platforms)

Update — Additional Color Direction
In addition to the dark charcoal/slate direction already described, I'm also interested in seeing variants with:
Dark navy blue — Deep, authoritative, intelligence-community feel. Same textured/matte treatment, not flat or bright.
Warm charcoal with steel blue accent — Keep the dark base but introduce a subtle steel blue gradient, accent line, or tonal shift. Sophisticated, modern, adds dimension without adding color noise.
Both should maintain the same premium, restrained, architectural feel described in the original brief. No bright blues, no corporate PowerPoint energy — think midnight, think depth, think weight.
Everything else in the brief remains the same.
I am building a premium personal brand as an executive advisor to founders ($5M+ revenue).
This contest is Facebook-banner–focused, but the design must represent a visual system that will be reused across:
- LinkedIn
- YouTube
I- nstagram
- X (Twitter)
- Website hero sections and other brand touchpoints
Think of the Facebook banner as the primary expression of the brand — not a one-off graphic.
This project is about discovering a high-end visual style and brand feel, not decoration.
What to design
Please submit one cohesive visual system, shown primarily as:
- Facebook banner (primary focus)
The same design language should clearly translate to all platforms listed above.
Designers are responsible for using the current recommended dimensions for each platform.
Quick clarification on background direction:
Backgrounds should have depth and texture, not flat color fields. Avoid pure white, light grey, or solid black backgrounds. Think matte, architectural materials — stone, graphite, concrete, steel — not blank canvases. Subtle tonal variation is encouraged. Obvious gradients or decorative patterns are not.
Text to use
Primary Headline:
- Your Business Is Too Valuable To Be Run On Hope.
Subheadline:
- You didn’t build a business to become its prisoner.
Name:
Paul Whitaker
The headline should be the dominant visual element.
Logo note (important)
My personal logo is currently being finalized.
For this contest:
- Use a simple “PW” monogram placeholder
- Clean, bold, geometric sans-serif
- Do not design a logo
- The winning design must allow an easy logo swap later.
Headshot note (important)
- Please do not include a headshot in the banner design.
- Most platforms display a circular profile image separately.
- The banner should stand on its own using typography, layout, and tone only.
- Design the banner assuming the profile photo will sit nearby, not inside the banner.
Style direction
The design should feel:
- Premium
- Calm
- Confident
- Restrained
- High-trust
- Dark, neutral backgrounds are preferred.
- Fewer elements are better than more.
Think:
- Owner-level advisor
- Private equity / boardroom tone
- Industrial, Modern, Minimalist, Elite, Architectural, not decorative
What to avoid
Please do not submit designs that feel:
- Promotional, hype-driven, or salesy
- Like a coach, guru, or agency
- Bright, colorful, or gradient-heavy
- Busy or over-designed
- Based on stock photos
- No motivational speaker energy.
Reaction test
- If someone sees this banner on Facebook (or later on LinkedIn, YouTube, etc.), the reaction should be:
“That person is serious. I’d trust them with important decisions.”
Final note
- I am not looking for many variations.
- I am looking for one strong visual direction you believe in.
Simple beats clever.
- Restraint beats decoration.

```html
<!DOCTYPE html>
<html lang="en">
<head>
<meta charset="UTF-8">
<title>Paul Whitaker — Banner</title>
<link rel="stylesheet" href="https://fonts.googleapis.com/css2?family=Anton&family=Oswald:wght@500;600&display=swap">
<style>
  :root {
    --page: #ffffff;
    --charcoal-deep: #1b1c1e;
    --charcoal: #2a2b2e;
    --charcoal-warm: #34312f;
    --steel: #5d7a95;
    --steel-deep: #3f5870;
    --ink-light: #ecebe8;
    --ink-muted: #a9b4be;
  }
  * { margin: 0; padding: 0; box-sizing: border-box; }
  html, body {
    width: 1200px;
    height: 1200px;
    overflow: hidden;
    background: var(--page);
  }
  .banner {
    position: absolute;
    left: 108px;
    top: 384px;
    width: 982px;
    height: 432px;
    overflow: hidden;
  }
  .banner-backdrop {
    position: absolute;
    inset: 0;
    background:
      radial-gradient(ellipse at 30% 40%, rgba(255,255,255,0.05) 0%, rgba(255,255,255,0) 60%),
      linear-gradient(135deg, var(--charcoal-warm) 0%, var(--charcoal) 50%, var(--charcoal-deep) 100%);
  }
  .growth-arrow {
    position: absolute;
    inset: 0;
    width: 982px;
    height: 432px;
  }
  .growth-arrow .arrow-name {
    font-family: "Anton", "Impact", sans-serif;
    font-size: 22px;
    letter-spacing: 1px;
    fill: var(--ink-light);
  }
  .headline {
    position: absolute;
    left: 138px;
    top: 68px;
    font-family: "Anton", "Impact", sans-serif;
    font-weight: 400;
    font-size: 68px;
    line-height: 58px;
    letter-spacing: 3px;
    color: var(--ink-light);
    text-transform: uppercase;
  }
  .headline .highlight { color: var(--steel); }
  .subheadline {
    position: absolute;
    left: 139px;
    top: 258px;
    font-family: "Oswald", "Arial Narrow", sans-serif;
    font-weight: 500;
    font-size: 19px;
    letter-spacing: 0.2px;
    color: var(--ink-muted);
  }
  .monogram {
    position: absolute;
    right: 40px;
    bottom: 30px;
    display: flex;
    align-items: center;
    gap: 10px;
  }
  .monogram-mark {
    width: 14px;
    height: 14px;
    background: var(--steel);
  }
  .monogram-text {
    font-family: "Anton", "Impact", sans-serif;
    font-size: 30px;
    line-height: 1;
    letter-spacing: 2px;
    color: var(--ink-light);
  }
</style>
</head>
<body>
  <section class="banner">
    <div class="banner-backdrop" role="img" aria-label="Dark matte graphite wall texture"></div>

    <svg class="growth-arrow" viewBox="0 0 982 432" aria-hidden="true">
      <polyline points="150,470 186,432 336,324 380,372 540,318 566,372 852,129"
                fill="none" stroke="var(--steel-deep)" stroke-width="36" stroke-linejoin="miter" stroke-miterlimit="6"/>
      <polygon points="906,84 880,164 824,98" fill="var(--steel-deep)"/>
      <text class="arrow-name" x="0" y="0" text-anchor="middle" dominant-baseline="middle"
            transform="translate(722,240) rotate(-40)">PAUL WHITAKER</text>
    </svg>

    <h1 class="headline">
      Your <span class="highlight">Business</span> Is<br>
      Too <span class="highlight">Valuable</span> To<br>
      Be Run On <span class="highlight">Hope.</span>
    </h1>
    <p class="subheadline">You didn’t build a business to become its prisoner.</p>

    <div class="monogram" aria-label="Paul Whitaker monogram placeholder">
      <span class="monogram-mark"></span>
      <span class="monogram-text">PW</span>
    </div>
  </section>
</body>
</html>
```